Modern business card design for professional copywriter

I'd like a business card design that I can use to have my cards printed out by tavrel.com as a squared corners business card (see artwork and design guidelines here: https://help.tavrel.com/hc/en-gb/sections/300481762-TAVREL-Product-Templates)

The design should be clean and modern and reflect the colours, tone and branding on my website: https://gretafolvane.com.au

Target Market(s)

Professionals, B2B small business owners

Industry/Entity Type

Business

Contact Information for Business Card

Greta Folvane
m: 0427 954 368
e: greta@gretafolvane.com.au
w: gretafolvane.com.au

Font styles to use
Sans Serif

Requirements
Must have
• Tagline: "Smart copywriting for clever business people"
• Brand colours: fd8000, 009984, 666666 and black
Nice to have

```html
<!DOCTYPE html>
<html lang="en">
<head>
<meta charset="utf-8">
<title>Greta Folvane Copywriter – Business Card</title>
<link rel="stylesheet" href="https://fonts.googleapis.com/css2?family=Open+Sans:wght@400;600;700&display=swap">
<style>
  :root {
    --teal: #009984;
    --orange: #fd8000;
    --grey: #666666;
    --ink: #111111;
    --paper: #ffffff;
    --backdrop: #e9e9ec;
    --map-tint: #0a8c78;
  }
  * { margin: 0; padding: 0; box-sizing: border-box; }
  html, body {
    width: 1200px; height: 934px; overflow: hidden;
    background: var(--backdrop);
    font-family: "Open Sans", Arial, sans-serif;
  }
  .canvas { position: relative; width: 1200px; height: 934px; }

  .card {
    position: absolute; left: 250px; width: 700px; height: 400px;
    overflow: hidden; box-shadow: 0 6px 18px rgba(0,0,0,0.12);
  }

  /* Back of card */
  .card-back { top: 47px; background: var(--teal); color: var(--paper); }
  .card-back .world-map {
    position: absolute; left: 70px; top: 30px; width: 560px; height: 280px;
    background: radial-gradient(ellipse at center, var(--map-tint) 0%, rgba(10,140,120,0) 70%);
  }
  .card-back .brand {
    position: absolute; left: 0; right: 0; top: 140px; text-align: center;
  }
  .card-back .brand-name {
    font-size: 46px; font-weight: 600; letter-spacing: -0.5px; line-height: 1;
  }
  .card-back .brand-role {
    margin-top: 6px; font-size: 15px; letter-spacing: 7px; padding-left: 150px;
  }
  .card-back .site {
    position: absolute; left: 0; right: 0; bottom: 34px; text-align: center;
    font-size: 15px; font-weight: 600;
  }

  /* Front of card */
  .card-front { top: 487px; background: var(--paper); }
  .card-front .brand { position: absolute; left: 42px; top: 88px; }
  .card-front .brand-name {
    font-size: 42px; font-weight: 600; color: var(--teal); letter-spacing: -0.5px; line-height: 1;
  }
  .card-front .brand-role {
    margin-top: 4px; font-size: 13px; letter-spacing: 6px; color: var(--grey); padding-left: 120px;
  }
  .card-front .holder { position: absolute; right: 40px; top: 96px; text-align: right; }
  .card-front .holder-name { font-size: 19px; font-weight: 700; color: var(--teal); }
  .card-front .holder-title {
    font-size: 13px; color: var(--grey);
    border-top: 1px solid var(--grey); padding-top: 1px; margin-left: 20px;
  }
  .card-front .divider { position: absolute; left: 0; top: 0; }

  .contacts { position: absolute; left: 42px; top: 262px; list-style: none; }
  .contacts li {
    display: flex; align-items: center; gap: 10px;
    font-size: 15px; color: var(--ink); line-height: 24px;
  }
  .contacts .icon {
    width: 17px; height: 17px; border-radius: 50%; background: var(--orange);
    display: flex; align-items: center; justify-content: center;
  }

  .bands { position: absolute; left: 0; bottom: 0; }
  .tagline {
    position: absolute; left: 30px; bottom: 9px;
    font-size: 15px; letter-spacing: 0.5px; color: var(--paper); text-transform: uppercase;
  }
</style>
</head>
<body>
<main class="canvas">

  <section class="card card-back" aria-label="Card back">
    <div class="world-map" role="img" aria-label="Faint world map in darker teal"></div>
    <div class="brand">
      <div class="brand-name">Greta Folvane</div>
      <div class="brand-role">COPYWRITER</div>
    </div>
    <div class="site">www.gretafolvane.com.au</div>
  </section>

  <section class="card card-front" aria-label="Card front">
    <svg class="divider" width="700" height="400" viewBox="0 0 700 400" aria-hidden="true">
      <line x1="42" y1="252" x2="660" y2="140" stroke="#666666" stroke-width="1.2"/>
    </svg>

    <div class="brand">
      <div class="brand-name">Greta Folvane</div>
      <div class="brand-role">COPYWRITER</div>
    </div>

    <div class="holder">
      <div class="holder-name">Greta Folvane</div>
      <div class="holder-title">Owner</div>
    </div>

    <ul class="contacts">
      <li>
        <span class="icon"><svg width="9" height="11" viewBox="0 0 9 11"><rect x="1.5" y="0.5" width="6" height="10" rx="1" fill="none" stroke="#fff" stroke-width="1.2"/></svg></span>
        0427 954 368
      </li>
      <li>
        <span class="icon"><svg width="10" height="8" viewBox="0 0 10 8"><rect x="0.6" y="0.6" width="8.8" height="6.8" fill="none" stroke="#fff" stroke-width="1.1"/><polyline points="0.6,0.6 5,4.5 9.4,0.6" fill="none" stroke="#fff" stroke-width="1.1"/></svg></span>
        greta@gretafolvane.com.au
      </li>
      <li>
        <span class="icon"><svg width="11" height="11" viewBox="0 0 11 11"><circle cx="5.5" cy="5.5" r="4.5" fill="none" stroke="#fff" stroke-width="1.1"/><ellipse cx="5.5" cy="5.5" rx="2" ry="4.5" fill="none" stroke="#fff" stroke-width="1"/><line x1="1" y1="5.5" x2="10" y2="5.5" stroke="#fff" stroke-width="1"/></svg></span>
        www.gretafolvane.com.au
      </li>
    </ul>

    <svg class="bands" width="700" height="80" viewBox="0 0 700 80" aria-hidden="true">
      <polygon points="0,46 470,46 450,80 0,80" fill="#009984"/>
      <polygon points="490,28 700,28 700,56 476,56" fill="#fd8000"/>
    </svg>
    <div class="tagline">Smart copywriting for clever business people</div>
  </section>

</main>
</body>
</html>
```